Building certification business in Sydney Australia

Brookvale Assessors is a small business that is currently growing and needs a profession looking website to attract customers and give them all the information they need. The main services we offer currently are pre-purchase building inspections for purchasers and other areas of construction consultancy including pool fencing certificates. Please see attached logos to incorporate to also match colour schemes with. Thanks!

Target Market(s)

Prospective buyers and home owners

Industry/Entity Type

Small Business

Requirements
Must have
• Promote the main services from the home page. Being able to select the type of service/certificate required from the main page and be directed to a specific page that deals with only that service containing the relevant information for that item.
Nice to have
• Small emphasis on the location of our office and areas we service etc.

```html
<!DOCTYPE html>
<html lang="en">
<head>
<meta charset="utf-8">
<title>Brookvale Assessors – Building Inspections</title>
<link href="https://fonts.googleapis.com/css2?family=Arimo:wght@400;700&family=Roboto+Slab:wght@500;700&display=swap" rel="stylesheet">
<style>
:root{
  --page:#e8e4d8;
  --navy:#22344a;
  --navy-dark:#1b2a3c;
  --blue:#1e7dc1;
  --blue-light:#2f95d8;
  --white:#ffffff;
  --ink:#333333;
  --line:#d9d6cf;
  --icon:#2a4d75;
}
*{margin:0;padding:0;box-sizing:border-box}
html,body{width:1200px;height:1021px;overflow:hidden}
body{position:relative;background:var(--page);font-family:"Arimo",Arial,sans-serif;color:var(--ink)}
.abs{position:absolute}

/* header */
.nav-band{left:0;top:76px;width:1200px;height:50px;background:var(--navy);border-top:2px dotted #8a97a6;border-bottom:2px dotted #8a97a6;box-shadow:0 2px 0 var(--navy-dark)}
.logo-box{left:128px;top:29px;width:239px;height:109px;background:var(--white);box-shadow:2px 3px 5px rgba(0,0,0,.35);display:flex;align-items:center;padding-left:22px;gap:10px}
.logo-mark{width:34px;height:34px;border:5px solid var(--blue);border-radius:5px;flex:none}
.logo-name{font-weight:700;font-size:24px;line-height:26px;color:var(--navy)}
.contact-line{left:625px;top:34px;font-size:12.5px;font-weight:700;color:#111;white-space:nowrap}
.contact-line .today{color:var(--blue);font-weight:400}
.contact-line .phone{font-family:"Roboto Slab",serif;font-size:19px;color:var(--blue);font-weight:500}
.book-btn{left:866px;top:28px;width:196px;height:28px;background:var(--blue);border-radius:4px;color:var(--white);font-family:"Roboto Slab",serif;font-weight:500;font-size:14.5px;line-height:28px;text-align:center;white-space:nowrap}
.home-icon{left:423px;top:87px;width:29px;height:29px;border-radius:50%;background:var(--blue);border:2px solid #9cc6e6}
.main-nav{top:92px;color:var(--white);font-weight:700;font-size:15px;white-space:nowrap}

/* hero */
.hero{left:129px;top:156px;width:937px;height:299px;box-shadow:0 8px 8px -4px rgba(0,0,0,.35);overflow:hidden}
.hero-photo{left:0;top:0;width:937px;height:299px;background:linear-gradient(180deg,#dfe3e4 0%,#c9ced0 30%,#7fa153 60%,#5e8a35 100%)}
.hero-text{left:21px;top:42px;width:296px;font-family:"Roboto Slab",serif;font-weight:700;font-size:26px;line-height:35px;color:var(--white)}
.slider-dots{left:21px;top:276px;display:flex;gap:4px}
.slider-dots span{width:10px;height:10px;background:#c9ced3}
.slider-dots span.on{background:var(--navy)}

/* call to action strip */
.cta-strip{left:129px;top:481px;width:941px;height:64px;border-radius:12px;background:linear-gradient(90deg,#eeeeec,#ffffff 55%,#f3f3f1);box-shadow:0 1px 2px rgba(0,0,0,.15)}
.cta-title{left:14px;top:10px;font-weight:700;font-size:20px;color:#444;white-space:nowrap}
.cta-sub{left:16px;top:37px;font-size:13px;color:#333;white-space:nowrap}
.cta-btn{left:669px;top:10px;width:252px;height:47px;border-radius:4px;background:linear-gradient(180deg,var(--blue-light),#1870ae);border:1px solid #145e92;color:var(--white);font-weight:700;font-size:23px;line-height:45px;padding-left:56px;white-space:nowrap}
.cta-arrow{left:10px;top:8px}

/* cards */
.card{top:585px;width:301px;height:307px;background:linear-gradient(180deg,#fbfaf8,#eeedeb);border:1px solid var(--line)}
.card-tab{left:21px;top:-4px;width:161px;height:30px;background:var(--navy);border-radius:0 0 6px 6px;color:var(--white);font-weight:700;font-size:17px;line-height:30px;padding-left:18px;white-space:nowrap}
.read-more{right:14px;bottom:-4px;width:90px;height:25px;background:var(--blue);border-radius:5px 5px 0 0;color:var(--white);font-weight:700;font-size:13px;line-height:25px;text-align:center}
.welcome-photo{left:13px;top:15px;width:274px;height:141px;background:linear-gradient(90deg,#8fa3a0,#c9d2cf 45%,#6e7f86)}
.welcome-text{left:15px;top:176px;width:275px;font-size:13.3px;line-height:18.6px;color:#333}
.service-list{left:14px;top:50px;list-style:none;width:268px}
.service-list li{display:flex;gap:15px;font-size:15px;line-height:17.5px;color:#222;margin-bottom:17px}
.service-list li svg{flex:none;margin-top:-2px}
.field{left:14px;width:271px;background:var(--white);border:1px solid #dcdcdc;font-size:12px;color:#666;padding:11px 0 0 30px}
.field svg{position:absolute;left:9px;top:11px}

/* footer */
.footer{left:0;top:945px;width:1200px;height:76px;background:var(--navy);border-top:6px solid var(--blue)}
.footer-links{left:140px;top:18px;font-size:12.5px;color:var(--white);word-spacing:2px;white-space:nowrap}
.copyright{left:140px;top:47px;font-size:12.5px;color:var(--white);white-space:nowrap}
.social{top:26px;width:28px;height:28px;border-radius:50%}
</style>
</head>
<body>

<div class="abs nav-band"></div>

<div class="abs logo-box">
  <span class="logo-mark"></span>
  <span class="logo-name">Brookvale<br>Assessors</span>
</div>

<div class="abs contact-line">Contact us <span class="today">Today :</span> <span class="phone">555-018-2640</span></div>
<div class="abs book-btn">BOOK AN INSPECTION</div>

<div class="abs home-icon">
  <svg width="25" height="25" viewBox="0 0 25 25"><path d="M5 13 L12.5 6 L20 13 M8 12 V19 H17 V12" fill="none" stroke="#fff" stroke-width="2.4" stroke-linejoin="round"/></svg>
</div>
<nav>
  <span class="abs main-nav" style="left:499px">About Us</span>
  <span class="abs main-nav" style="left:610px">Services</span>
  <span class="abs main-nav" style="left:716px">Our Consultants</span>
  <span class="abs main-nav" style="left:875px">Pricing</span>
  <span class="abs main-nav" style="left:969px">Contact Us</span>
</nav>

<section class="abs hero">
  <div class="abs hero-photo" role="img" aria-label="Smiling family of three sitting on the lawn in front of a white house"></div>
  <svg class="abs" style="left:0;top:0" width="937" height="299" viewBox="0 0 937 299">
    <path d="M0 0 H442 C380 40 330 120 280 299 H0 Z" fill="var(--blue)"/>
  </svg>
  <h1 class="abs hero-text">We offer pre-purchase building inspections &amp; combined pre-purchase building &amp; pest inspections</h1>
  <div class="abs slider-dots"><span class="on"></span><span></span><span></span><span></span></div>
</section>

<section class="abs cta-strip">
  <h2 class="abs cta-title">Lorem ipsum dolor sit amet consectetuer adipiscing adipiscin</h2>
  <p class="abs cta-sub">consectetuer adipiscing elit, sed diam nonummy nibh euismod tincidunt</p>
  <div class="abs cta-btn">
    <svg class="abs cta-arrow" width="30" height="30" viewBox="0 0 30 30"><path d="M3 11 H15 V4 L27 15 L15 26 V19 H3 Z" fill="#7cc242"/></svg>
    <span class="abs" style="left:45px;top:6px;width:1px;height:33px;background:#5aa8dc"></span>
    Get Started Now!
  </div>
</section>

<section class="abs card" style="left:129px">
  <div class="abs welcome-photo" role="img" aria-label="Smiling businesswoman in a dark suit standing in an office corridor"></div>
  <h3 class="abs card-tab">Welcome to BA</h3>
  <p class="abs welcome-text">Lorem ipsum dolor sit amet, consectetuer adipiscing elit, sed diam nonummy nibh euismod tcidunt ut laoreet dolore magna aliquam erat volutpat. Ut wisi enim ad minim veniam, quis nostrud exerci tation</p>
  <span class="abs read-more">Read More</span>
</section>

<section class="abs card" style="left:449px">
  <h3 class="abs card-tab">BA Services</h3>
  <ul class="abs service-list">
    <li><svg width="20" height="22" viewBox="0 0 20 22"><rect x="1" y="5" width="15" height="15" rx="2" fill="none" stroke="var(--icon)" stroke-width="2"/><path d="M5 12 L9 17 L17 2" fill="none" stroke="var(--icon)" stroke-width="2.2"/></svg>Complete Pre-purchase Building Inspection</li>
    <li><svg width="20" height="22" viewBox="0 0 20 22"><rect x="1" y="5" width="15" height="15" rx="2" fill="none" stroke="var(--icon)" stroke-width="2"/><path d="M5 12 L9 17 L17 2" fill="none" stroke="var(--icon)" stroke-width="2.2"/></svg>Structural Plus Pre-purchase Building Inspection</li>
    <li><svg width="20" height="22" viewBox="0 0 20 22"><rect x="1" y="5" width="15" height="15" rx="2" fill="none" stroke="var(--icon)" stroke-width="2"/><path d="M5 12 L9 17 L17 2" fill="none" stroke="var(--icon)" stroke-width="2.2"/></svg>Combined Building &amp; Pest Inspection</li>
    <li><svg width="20" height="22" viewBox="0 0 20 22"><rect x="1" y="5" width="15" height="15" rx="2" fill="none" stroke="var(--icon)" stroke-width="2"/><path d="M5 12 L9 17 L17 2" fill="none" stroke="var(--icon)" stroke-width="2.2"/></svg>Pool Safety Inspection</li>
    <li><svg width="20" height="22" viewBox="0 0 20 22"><rect x="1" y="5" width="15" height="15" rx="2" fill="none" stroke="var(--icon)" stroke-width="2"/><path d="M5 12 L9 17 L17 2" fill="none" stroke="var(--icon)" stroke-width="2.2"/></svg>Defects Liability Period Inspection</li>
  </ul>
  <span class="abs read-more">Read More</span>
</section>

<section class="abs card" style="left:769px">
  <h3 class="abs card-tab">Quick Inquiry</h3>
  <div class="abs field" style="top:45px;height:34px">
    <svg width="12" height="12" viewBox="0 0 12 12"><circle cx="6" cy="3.5" r="3" fill="#999"/><path d="M0 12 C0 7 12 7 12 12 Z" fill="#999"/></svg>Name</div>
  <div class="abs field" style="top:86px;height:34px">
    <svg width="14" height="10" viewBox="0 0 14 10"><rect x=".5" y=".5" width="13" height="9" fill="none" stroke="#999"/><path d="M.5 .5 L7 6 L13.5 .5" fill="none" stroke="#999"/></svg>Email</div>
  <div class="abs field" style="top:129px;height:138px">
    <svg width="13" height="13" viewBox="0 0 13 13"><rect x=".5" y="2.5" width="10" height="10" fill="none" stroke="#999"/><path d="M5 8 L12 1" stroke="#999" stroke-width="2"/></svg>Message</div>
  <span class="abs read-more">Read More</span>
</section>

<footer class="abs footer">
  <p class="abs footer-links">Home &nbsp;|&nbsp; About Us &nbsp;|&nbsp; Services &nbsp;|&nbsp; Our Consultants &nbsp;|&nbsp; Pricing &nbsp;|&nbsp; Contact Us</p>
  <p class="abs copyright">© Copyright 2014 BrookvaleAssessors &nbsp;&nbsp;|&nbsp;&nbsp; All Rights Reserved</p>
  <span class="abs social" style="left:965px;background:#3bc2ee" aria-label="Social profile"></span>
  <span class="abs social" style="left:1003px;background:#3d63ad" aria-label="Social profile"></span>
  <span class="abs social" style="left:1040px;background:#2a8cc8" aria-label="Social profile"></span>
</footer>

</body>
</html>
```